Design a Future- POV DKVANTOM

Refresh the images/Theme. Focus theme/images on the following

1. Adaptability
2. Resilience
3. Emotional Inteligence
4. Relentless execution
5. High Care Factor

Industry/Entity Type

Technology Equipment

Font styles to use
Other font styles liked:
• Corvex Sans

Colors
33a6d7
cfdeed
85acd3
85cae6
fcf7c1
3377b5
fee18a

Requirements
Must have
• Consistent theme
Professional almost marketing look and feel
Nice to have
• none
Should not have
• none

```html
<!DOCTYPE html>
<html lang="en">
<head>
<meta charset="utf-8">
<title>Future POV – DKVANTOM – Slide Deck</title>
<link rel="stylesheet" href="https://fonts.googleapis.com/css2?family=Montserrat:wght@400;500;600;700&family=Open+Sans:wght@400;600;700&display=swap">
<style>
:root{
  --navy:#123b73;
  --deep:#1c4f8e;
  --blue:#3377b5;
  --sky:#33a6d7;
  --aqua:#85cae6;
  --steel:#85acd3;
  --mist:#cfdeed;
  --cream:#fcf7c1;
  --gold:#fee18a;
  --ink:#1d2b44;
  --text:#4a5568;
  --page:#efeff1;
  --white:#ffffff;
}
*{box-sizing:border-box;margin:0;padding:0}
html,body{width:1200px;height:3920px;overflow:hidden;background:var(--page)}
body{font-family:"Open Sans",Arial,sans-serif;color:var(--text)}
.deck{position:absolute;left:33px;top:58px;display:grid;grid-template-columns:554px 554px;grid-template-rows:repeat(11,312px);column-gap:26px;row-gap:37px}
.slide{position:relative;width:554px;height:312px;overflow:hidden;background:var(--white);box-shadow:0 3px 10px rgba(20,40,80,.18)}
.abs{position:absolute}
.photo{position:absolute}
.h-font{font-family:"Montserrat",Arial,sans-serif}
svg.ic{display:block;width:100%;height:100%;fill:none;stroke:currentColor;stroke-width:1.6;stroke-linecap:round;stroke-linejoin:round}

/* social dots */
.social{position:absolute;top:10px;display:flex;gap:3px}
.social i{display:block;width:9px;height:9px;border:1px solid rgba(255,255,255,.85);border-radius:50%}
.social.dark i{border-color:#8a94a6}

/* cover */
.cover{position:absolute;inset:0;display:flex;flex-direction:column;align-items:center;color:var(--white)}
.cover .title-box{margin-top:110px;border:2px solid var(--white);padding:1px 10px 2px;font-family:"Montserrat",sans-serif;font-weight:600;font-size:25px;line-height:30px}
.cover .sub{margin-top:8px;font-family:"Montserrat",sans-serif;font-size:8.5px;letter-spacing:.4px}
.cover .badge{margin-top:18px;width:26px;height:26px;border:1.5px solid var(--white);border-radius:50%;padding:5px}
.pill{display:inline-block;background:var(--white);color:var(--deep);font-family:"Montserrat",sans-serif;font-weight:600;font-size:8px;letter-spacing:.6px;border-radius:12px;padding:5px 0;width:112px;text-align:center}
.cover .pill{margin-top:12px}
.cover .date{position:absolute;bottom:12px;font-family:"Montserrat",sans-serif;font-weight:600;font-size:8px}

/* header band */
.head{position:absolute;left:0;top:0;width:484px;height:48px;background:linear-gradient(90deg,var(--sky),var(--blue));border-bottom-right-radius:60px}
.head-sweep{position:absolute;left:0;top:40px;width:120px;height:40px;background:linear-gradient(180deg,var(--blue),rgba(51,166,215,0));clip-path:polygon(0 0,100% 0,0 100%)}
.head h2{position:absolute;left:50px;top:12px;color:var(--white);font-family:"Montserrat",sans-serif;font-weight:600;font-size:18px;line-height:24px}

.ring{position:absolute;display:block;width:24px;height:24px;border:1.3px solid var(--deep);border-radius:50%;padding:5px;color:var(--deep)}
.blue-disc{position:absolute;display:block;border-radius:50%;background:radial-gradient(circle at 35% 30%,var(--sky),var(--blue));color:var(--white);box-shadow:0 2px 6px rgba(20,60,120,.35);border:2px solid var(--white)}
.label{position:absolute;font-size:9.5px;color:var(--ink)}
.tiny{font-size:6px;line-height:8px;color:var(--text)}
.card{position:absolute;background:var(--white);border-radius:8px;box-shadow:0 2px 8px rgba(20,40,80,.2)}

/* agenda */
.agenda-list{position:absolute;left:68px;top:64px;list-style:none}
.agenda-list li{position:relative;height:39px;padding-left:40px;line-height:24px;font-size:9.5px;color:var(--ink)}
.agenda-list .ring{left:0;top:0}

/* 30-60-90 */
.plan-card{position:absolute;top:110px;width:140px;height:160px;background:var(--white);border-radius:8px;box-shadow:0 2px 8px rgba(20,40,80,.22);text-align:center;padding-top:38px}
.plan-card h4{font-family:"Montserrat",sans-serif;font-weight:700;font-size:10px;color:var(--ink);margin-bottom:10px}
.plan-card p{font-size:7px;line-height:11px;color:var(--ink)}
.plan-card p.b{color:var(--blue)}
.plan-card .rule{position:absolute;top:28px;bottom:16px;width:1px;background:var(--steel)}
.hex{position:absolute;display:block;top:-24px;left:48px;width:44px;height:48px;clip-path:polygon(50% 0,100% 25%,100% 75%,50% 100%,0 75%,0 25%);background:linear-gradient(180deg,var(--sky),var(--blue));padding:13px 11px;color:var(--white)}

/* FY */
.fy-col{position:absolute;top:58px;width:56px;text-align:center}
.fy-col .blue-disc{position:relative;width:44px;height:44px;padding:10px;margin:0 auto}
.fy-col .blue-disc.dark{background:radial-gradient(circle at 35% 30%,#2c5f9f,var(--navy))}
.fy-col .box{margin-top:10px;height:60px;border-radius:5px;box-shadow:0 2px 6px rgba(20,40,80,.2);font-size:6.8px;line-height:8.5px;color:var(--ink);display:flex;align-items:center;justify-content:center;padding:0 3px;background:var(--white)}
.fy-col .drop{margin:0 auto;width:1px;height:50px;border-left:1px dashed #98a4b6}

/* sponsors */
.sponsor{position:absolute;top:112px;width:100px;text-align:center}
.sponsor .face{width:64px;height:64px;border-radius:50%;margin:0 auto;background:linear-gradient(160deg,#d9dde3,#8a93a0);border:2px solid var(--white)}
.sponsor h5{margin-top:10px;font-family:"Montserrat",sans-serif;font-weight:700;font-size:9px;color:var(--deep)}
.sponsor p{font-size:6px;line-height:7.5px;color:var(--ink);margin-top:2px}

/* expectations chevrons */
.chev{position:absolute;top:88px;height:190px}
.chev > svg.shape{position:absolute;inset:0;width:100%;height:100%}
.chev .inner{position:absolute;inset:0;padding:14px 30px 0 34px;text-align:center}
.chev h5{font-family:"Montserrat",sans-serif;font-weight:700;font-size:8.5px;line-height:10px;color:var(--ink)}
.chev .icon{width:24px;height:24px;margin:8px auto 10px;color:var(--deep)}
.chev ul{text-align:left;font-size:6.2px;line-height:7.8px;color:var(--ink);padding-left:8px}

/* timeline */
.tl-year{position:absolute;left:248px;width:50px;height:16px;border-radius:8px;background:var(--white);box-shadow:0 1px 4px rgba(20,40,80,.25);font-family:"Montserrat",sans-serif;font-weight:700;font-size:7.5px;color:var(--ink);text-align:center;line-height:16px}
.tl-year.now{background:var(--blue);color:var(--white)}
.tl-text{position:absolute;left:318px;width:220px;font-size:7px;line-height:9px;color:var(--ink)}
.tl-logo{position:absolute;left:128px;width:108px;font-family:"Montserrat",sans-serif;font-weight:600;font-size:10px;color:var(--ink);display:flex;align-items:center;justify-content:flex-end;gap:4px;white-space:nowrap}
.tl-logo i{display:block;width:9px;height:9px;border-radius:50%;background:var(--blue)}
</style>
</head>
<body>

<svg width="0" height="0" style="position:absolute" aria-hidden="true">
  <defs>
    <symbol id="i-person" viewBox="0 0 24 24"><circle cx="12" cy="8" r="4"/><path d="M4 21c1-5 4-7 8-7s7 2 8 7"/></symbol>
    <symbol id="i-people" viewBox="0 0 24 24"><circle cx="7" cy="8" r="2.5"/><circle cx="12" cy="7" r="2.5"/><circle cx="17" cy="8" r="2.5"/><path d="M3 17c0-3 2-5 4-5M21 17c0-3-2-5-4-5M8 19c0-4 2-6 4-6s4 2 4 6"/></symbol>
    <symbol id="i-target" viewBox="0 0 24 24"><circle cx="12" cy="12" r="8"/><circle cx="12" cy="12" r="4"/><path d="M12 2v5M12 17v5M2 12h5M17 12h5"/></symbol>
    <symbol id="i-chart" viewBox="0 0 24 24"><path d="M3 20h18M6 16l4-5 3 3 6-8"/><path d="M15 6h4v4"/></symbol>
    <symbol id="i-gauge" viewBox="0 0 24 24"><circle cx="12" cy="12" r="9"/><path d="M12 12l4-4M7 12h1M12 6v1M16 12h1"/></symbol>
    <symbol id="i-puzzle" viewBox="0 0 24 24"><rect x="3" y="3" width="8" height="8"/><rect x="13" y="3" width="8" height="8"/><rect x="3" y="13" width="8" height="8"/><rect x="13" y="13" width="8" height="8"/></symbol>
    <symbol id="i-doc" viewBox="0 0 24 24"><path d="M6 3h9l4 4v14H6z"/><path d="M9 11h7M9 15h7M9 7h4"/></symbol>
    <symbol id="i-eye" viewBox="0 0 24 24"><path d="M2 12s4-7 10-7 10 7 10 7-4 7-10 7S2 12 2 12z"/><circle cx="12" cy="12" r="3"/></symbol>
    <symbol id="i-clock" viewBox="0 0 24 24"><circle cx="12" cy="12" r="9"/><path d="M12 7v5l3 2"/></symbol>
    <symbol id="i-building" viewBox="0 0 24 24"><rect x="4" y="4" width="10" height="17"/><path d="M14 10h6v11M7 8h4M7 12h4M7 16h4"/></symbol>
    <symbol id="i-trophy" viewBox="0 0 24 24"><path d="M8 4h8v5a4 4 0 0 1-8 0z"/><path d="M8 6H5c0 3 1 4 3 4M16 6h3c0 3-1 4-3 4M12 13v4M8 21h8M9 17h6"/></symbol>
    <symbol id="i-plane" viewBox="0 0 24 24"><path d="M21 3L3 11l7 2 2 7z"/><path d="M10 13l11-10"/></symbol>
    <symbol id="i-briefcase" viewBox="0 0 24 24"><rect x="3" y="7" width="18" height="13" rx="2"/><path d="M9 7V4h6v3M3 12h18"/></symbol>
    <symbol id="i-compass" viewBox="0 0 24 24"><circle cx="12" cy="12" r="9"/><path d="M15 9l-2 5-4 1 2-5z"/></symbol>
    <symbol id="i-triangle" viewBox="0 0 24 24"><path d="M12 4l9 16H3z"/><circle cx="12" cy="14" r="2.5"/></symbol>
    <symbol id="i-heart" viewBox="0 0 24 24"><path d="M12 20s-8-5-8-11a4 4 0 0 1 8-1 4 4 0 0 1 8 1c0 6-8 11-8 11z"/></symbol>
    <symbol id="i-paperclip" viewBox="0 0 24 24"><path d="M8 12l6-6a3 3 0 0 1 4 4l-8 8a5 5 0 0 1-7-7l7-7"/></symbol>
    <symbol id="i-medal" viewBox="0 0 24 24"><path d="M8 3l4 7 4-7"/><circle cx="12" cy="15" r="5"/></symbol>
  </defs>
</svg>

<main class="deck">

  <!-- 1 cover, sky -->
  <section class="slide">
    <div class="photo" style="inset:0;background:linear-gradient(160deg,#6fb4e4 0%,#3d8fd0 45%,#2a6fb8 100%)" role="img" aria-label="Upward view of glass office towers tinted blue"></div>
    <div class="social" style="left:256px"><i></i><i></i><i></i></div>
    <div class="cover">
      <div class="title-box">New Role</div>
      <div class="sub">POINT OF VIEW DOCUMENT</div>
      <div class="badge"><svg class="ic"><use href="#i-person"/></svg></div>
      <div class="pill">DKVANTOM</div>
      <div class="date">June 2020</div>
    </div>
  </section>

  <!-- 2 cover, royal -->
  <section class="slide">
    <div class="photo" style="inset:0;background:linear-gradient(160deg,#2c64ad 0%,#1f4f95 55%,#153d7a 100%)" role="img" aria-label="Upward view of office towers in deep blue tone"></div>
    <div class="social" style="left:256px"><i></i><i></i><i></i></div>
    <div class="cover">
      <div class="title-box">New Role</div>
      <div class="sub">POINT OF VIEW DOCUMENT</div>
      <div class="badge"><svg class="ic"><use href="#i-person"/></svg></div>
      <div class="pill">DKVANTOM</div>
      <div class="date">June 2020</div>
    </div>
  </section>

  <!-- 3 cover, night -->
  <section class="slide">
    <div class="photo" style="inset:0;background:radial-gradient(circle at 50% 40%,#25436d 0%,#15243d 60%,#0c1628 100%)" role="img" aria-label="Night view looking up between dark skyscrapers"></div>
    <div class="social" style="left:256px"><i></i><i></i><i></i></div>
    <div class="cover">
      <div class="title-box">New Role</div>
      <div class="sub">POINT OF VIEW DOCUMENT</div>
      <div class="badge"><svg class="ic"><use href="#i-person"/></svg></div>
      <div class="pill" style="color:var(--sky)">DKVANTOM</div>
      <div class="date">June 2020</div>
    </div>
  </section>

  <!-- 4 cover, light -->
  <section class="slide" style="background:#f4f4f5">
    <div class="photo" style="left:240px;top:0;right:0;bottom:0;background:linear-gradient(100deg,#f4f4f5 0%,#d9d9db 45%,#9a9a9e 100%)" role="img" aria-label="Black and white photo of hands typing on a laptop keyboard"></div>
    <div class="social dark" style="left:12px"><i></i><i></i><i></i></div>
    <div class="abs" style="left:14px;top:112px;width:2px;height:60px;background:var(--deep)"></div>
    <div class="abs h-font" style="left:26px;top:112px;font-weight:600;font-size:26px;color:#3a4250">New Role</div>
    <div class="abs h-font" style="left:26px;top:150px;font-size:8.5px;color:#3a4250">POINT OF VIEW DOCUMENT</div>
    <div class="abs h-font" style="left:12px;top:188px;font-size:8px;font-weight:600;color:#3a4250">June 2020</div>
    <div class="abs pill" style="left:12px;top:268px;color:var(--blue);border:1px solid var(--mist)">DKVANTOM</div>
  </section>

  <!-- 5 cover, feature image -->
  <section class="slide" style="background:linear-gradient(120deg,#1b3a66,#2a5fa3 70%,#3677bd)">
    <div class="photo" style="left:42px;top:52px;width:168px;height:214px;border-radius:12px;background:radial-gradient(circle at 55% 55%,#e79b4a 0%,#7a3a1c 35%,#1a1410 75%)" role="img" aria-label="Hand hovering over a glowing bar chart"></div>
    <div class="abs h-font" style="right:34px;top:46px;font-weight:600;font-size:29px;color:var(--white)">New Role</div>
    <div class="abs h-font" style="right:34px;top:86px;font-size:8.5px;color:var(--white)">POINT OF VIEW DOCUMENT</div>
    <div class="abs h-font" style="right:34px;top:114px;font-size:8px;font-weight:600;color:var(--white)">June 2020</div>
    <div class="abs pill" style="right:28px;top:140px">DKVANTOM</div>
    <div class="social" style="right:28px;top:280px"><i></i><i></i><i></i></div>
  </section>

  <!-- 6 agenda -->
  <section class="slide">
    <div class="head"><h2>AGENDA</h2></div>
    <div class="head-sweep"></div>
    <ul class="agenda-list">
      <li><span class="ring"><svg class="ic"><use href="#i-person"/></svg></span>About Me</li>
      <li><span class="ring"><svg class="ic"><use href="#i-compass"/></svg></span>Leadership Philosophy</li>
      <li><span class="ring"><svg class="ic"><use href="#i-medal"/></svg></span>Qualifications</li>
      <li><span class="ring"><svg class="ic"><use href="#i-clock"/></svg></span>30-60-90 Day Plan</li>
      <li><span class="ring"><svg class="ic"><use href="#i-building"/></svg></span>FY19 Success Defined</li>
      <li><span class="ring"><svg class="ic"><use href="#i-people"/></svg></span>Sponsors</li>
    </ul>
    <div class="photo" style="left:307px;top:67px;width:214px;height:228px;border-radius:22px;background:radial-gradient(circle at 50% 50%,#6f7580 0%,#c9ccd1 38%,#e4e5e8 70%)" role="img" aria-label="Globe wrapped in a network of connected points"></div>
  </section>

  <!-- 7 what matters -->
  <section class="slide">
    <div class="head"><h2>My “What Matters?”</h2></div>
    <div class="head-sweep"></div>
    <div class="abs" style="left:64px;top:66px;font-size:8px;color:var(--deep)">Servant Leadership &nbsp;|&nbsp; “Why We CAN” Mindset &nbsp;|&nbsp; Culture by Design &nbsp;|&nbsp; Golden Rule &nbsp;|&nbsp; Be Present</div>
    <div class="photo" style="left:8px;top:88px;width:98px;height:104px;background:linear-gradient(160deg,#c7cdd6,#59616e)" role="img" aria-label="Team photo outside an office building"></div>
    <div class="photo" style="left:108px;top:88px;width:128px;height:104px;background:linear-gradient(160deg,#8c7a6b,#2b2a30)" role="img" aria-label="Group photo at an evening event"></div>
    <div class="photo" style="left:238px;top:88px;width:96px;height:104px;background:linear-gradient(160deg,#dbe7ef,#6f8aa0)" role="img" aria-label="Team outdoors in winter"></div>
    <div class="photo" style="left:336px;top:88px;width:200px;height:104px;background:linear-gradient(160deg,#a9a298,#3b3a3d)" role="img" aria-label="Volunteer team at a food bank"></div>
    <div class="photo" style="left:8px;top:195px;width:146px;height:95px;background:linear-gradient(160deg,#57657a,#1e2533)" role="img" aria-label="Speaker presenting on stage"></div>
    <div class="photo" style="left:156px;top:195px;width:154px;height:95px;background:linear-gradient(160deg,#7a4fb3,#2c1f5a)" role="img" aria-label="Team at an evening celebration"></div>
    <div class="photo" style="left:312px;top:195px;width:146px;height:95px;background:linear-gradient(160deg,#e9ecef,#9aa3ad)" role="img" aria-label="Volunteers in white protective coats"></div>
    <div class="photo" style="left:460px;top:195px;width:76px;height:95px;background:linear-gradient(160deg,#c4b9a8,#5d5547)" role="img" aria-label="Person beside a landmark statue"></div>
  </section>

  <!-- 8 leadership philosophy -->
  <section class="slide">
    <div class="head"><h2>Leadership Philosophy</h2></div>
    <div class="head-sweep"></div>
    <div class="photo" style="left:28px;top:80px;width:206px;height:210px;border-radius:12px;background:linear-gradient(150deg,#5b7fae,#1d3f78 60%,#15305f)" role="img" aria-label="Hands reaching toward each other in blue light"></div>
    <div class="abs h-font" style="left:36px;top:82px;font-size:46px;font-weight:700;color:var(--white);line-height:46px">“</div>
    <div class="abs" style="left:60px;top:128px;width:150px;text-align:center;color:var(--white);font-size:9px;line-height:11.5px">Great leaders are almost always great simplifiers, who can cut through argument, debate and doubt to offer a solution everybody can understand.</div>
    <div class="abs" style="left:60px;top:218px;width:150px;text-align:center;color:var(--white);font-size:6.5px;line-height:8px;font-style:italic">— Gen. Marcus Hale, former U.S.<br>Secretary of State</div>
    <div class="abs h-font" style="left:200px;top:236px;font-size:46px;font-weight:700;color:var(--white);line-height:46px">”</div>
    <div class="abs" style="left:256px;top:82px;width:222px;height:22px;background:var(--white);box-shadow:0 1px 5px rgba(20,40,80,.2);clip-path:polygon(0 0,94% 0,100% 50%,94% 100%,0 100%);font-size:8px;line-height:22px;padding-left:16px;color:var(--deep)">My formula for <b>SUCCESS</b> has been:</div>
    <div class="abs" style="left:494px;top:72px;width:34px;height:34px;color:var(--deep)"><svg class="ic"><use href="#i-trophy"/></svg></div>
    <div class="abs" style="left:270px;top:110px;width:1px;height:176px;border-left:1px dashed var(--steel)"></div>
    <span class="ring" style="left:283px;top:125px"><svg class="ic"><use href="#i-person"/></svg></span>
    <div class="label" style="left:322px;top:131px;color:var(--deep)">Hiring great leaders</div>
    <span class="ring" style="left:283px;top:167px"><svg class="ic"><use href="#i-eye"/></svg></span>
    <div class="label" style="left:322px;top:173px;color:var(--deep)">Over communicating the stretch vision</div>
    <span class="ring" style="left:283px;top:209px"><svg class="ic"><use href="#i-chart"/></svg></span>
    <div class="label" style="left:322px;top:215px;color:var(--deep)">Making good, data-driven decisions</div>
    <span class="ring" style="left:283px;top:251px"><svg class="ic"><use href="#i-target"/></svg></span>
    <div class="label" style="left:322px;top:257px;color:var(--deep)">Finding ways to scale it</div>
  </section>

  <!-- 9 key capabilities -->
  <section class="slide">
    <div class="abs" style="left:-120px;top:-40px;width:350px;height:392px;border-radius:50%;background:linear-gradient(180deg,var(--sky),var(--blue))"></div>
    <div class="photo" style="left:-130px;top:-40px;width:340px;height:392px;border-radius:50%;background:radial-gradient(circle at 70% 50%,#4a5668 0%,#1f2734 55%,#121821 100%)" role="img" aria-label="Close-up of a vintage compass on dark wood"></div>
    <div class="abs h-font" style="left:24px;top:120px;font-weight:600;font-size:20px;line-height:24px;color:var(--white)">Key<br>Capabilities</div>
    <div class="abs" style="left:24px;top:173px;width:26px;height:2px;background:var(--white)"></div>
    <svg class="abs" style="left:300px;top:20px" width="80" height="280" viewBox="0 0 80 280" fill="none" stroke="#98a4b6" stroke-dasharray="3 3"><path d="M20 0 C60 70 60 200 20 280"/></svg>
    <span class="blue-disc" style="left:300px;top:30px;width:38px;height:38px;padding:9px"><svg class="ic"><use href="#i-eye"/></svg></span>
    <div class="label" style="left:350px;top:42px">Sense-making</div>
    <span class="blue-disc" style="left:328px;top:100px;width:38px;height:38px;padding:9px"><svg class="ic"><use href="#i-triangle"/></svg></span>
    <div class="label" style="left:378px;top:112px">Relating</div>
    <span class="blue-disc" style="left:328px;top:164px;width:38px;height:38px;padding:9px"><svg class="ic"><use href="#i-target"/></svg></span>
    <div class="label" style="left:378px;top:176px">Visioning</div>
    <span class="blue-disc" style="left:300px;top:237px;width:38px;height:38px;padding:9px"><svg class="ic"><use href="#i-briefcase"/></svg></span>
    <div class="label" style="left:350px;top:249px">Inventing</div>
  </section>

  <!-- 10 why me -->
  <section class="slide">
    <div class="head"><h2>Why Me &amp; Why This Role</h2></div>
    <div class="head-sweep"></div>
    <div class="abs" style="left:24px;top:84px;width:510px;display:flex;justify-content:space-between">
      <div style="width:80px;height:80px;border-radius:50%;border:3px solid var(--gold);display:flex;align-items:center;justify-content:center;text-align:center;font-size:7px;line-height:9px;color:var(--ink);padding:10px">Market leader for CSR</div>
      <div style="width:80px;height:80px;border-radius:50%;border:3px solid var(--gold);display:flex;align-items:center;justify-content:center;text-align:center;font-size:7px;line-height:9px;color:var(--ink);padding:10px">Executive Sponsor PHL Connected Women</div>
      <div style="width:80px;height:80px;border-radius:50%;border:3px solid var(--gold);display:flex;align-items:center;justify-content:center;text-align:center;font-size:7px;line-height:9px;color:var(--ink);padding:10px">Leadership Instructor, Harbor Guard</div>
      <div style="width:80px;height:80px;border-radius:50%;border:3px solid var(--gold);display:flex;align-items:center;justify-content:center;text-align:center;font-size:7px;line-height:9px;color:var(--ink);padding:10px">Manager Excellence &amp; Presidents Club</div>
      <div style="width:80px;height:80px;border-radius:50%;border:3px solid var(--gold);display:flex;align-items:center;justify-content:center;text-align:center;font-size:7px;line-height:9px;color:var(--ink);padding:10px">Passionate Mentor and Sponsor</div>
    </div>
    <div class="card" style="left:22px;top:196px;width:150px;height:100px;padding:26px 8px 0">
      <span class="blue-disc" style="left:56px;top:-20px;width:36px;height:36px;padding:8px"><svg class="ic"><use href="#i-target"/></svg></span>
      <div class="h-font" style="font-weight:700;font-size:7.5px;color:var(--ink);text-align:center;margin-bottom:6px">Track record of Success &amp; Leadership</div>
      <ul class="tiny" style="padding-left:8px"><li>History of exceeding growth targets</li><li>Selected for and implemented leadership programs</li><li>Proven adaptability</li></ul>
    </div>
    <div class="card" style="left:202px;top:196px;width:150px;height:100px;padding:26px 8px 0">
      <span class="blue-disc" style="left:56px;top:-20px;width:36px;height:36px;padding:8px"><svg class="ic"><use href="#i-compass"/></svg></span>
      <div class="h-font" style="font-weight:700;font-size:7.5px;color:var(--ink);text-align:center;margin-bottom:6px">Diverse Industry &amp; Role Experience</div>
      <ul class="tiny" style="padding-left:18px"><li>Software &amp; CX Background</li><li>IT Services Sales</li><li>Refugee Operations in Cuba</li></ul>
    </div>
    <div class="card" style="left:382px;top:196px;width:150px;height:100px;padding:26px 8px 0">
      <span class="blue-disc" style="left:56px;top:-20px;width:36px;height:36px;padding:8px"><svg class="ic"><use href="#i-people"/></svg></span>
      <div class="h-font" style="font-weight:700;font-size:7.5px;color:var(--ink);text-align:center;margin-bottom:6px">Think Big &amp; Act Small</div>
      <ul class="tiny" style="padding-left:18px"><li>Culture Builder</li><li>Model Optimization</li><li>Program Development &amp; Execution</li></ul>
    </div>
  </section>

  <!-- 11 30-60-90 -->
  <section class="slide">
    <div class="abs" style="right:0;top:0;width:260px;height:312px;background:linear-gradient(200deg,var(--sky) 0%,rgba(51,166,215,.3) 30%,rgba(255,255,255,0) 55%)"></div>
    <div class="abs h-font" style="left:46px;top:16px;font-weight:700;font-size:17px;color:var(--ink)">30-60-90 Day Plan</div>
    <div class="abs" style="left:46px;top:42px;width:56px;height:2px;background:var(--sky)"></div>
    <div class="plan-card" style="left:44px"><span class="hex"><svg class="ic"><use href="#i-people"/></svg></span><span class="rule" style="left:8px"></span>
      <h4>PEOPLE</h4><p>Build Trust</p><p class="b">Market Visits - Town Hall</p><p>Leadership Team</p><p class="b">Direct Teams</p><p>Engineering Team</p><p class="b">Dotted line resources</p></div>
    <div class="plan-card" style="left:207px"><span class="hex"><svg class="ic"><use href="#i-doc"/></svg></span><span class="rule" style="left:8px"></span>
      <h4>PIPELINE</h4><p>90 day Pipeline</p><p class="b">Key Deals</p><p>Qtr Event Calendar</p><p class="b">Portfolio Balance</p><p>2X2</p></div>
    <div class="plan-card" style="left:370px"><span class="hex"><svg class="ic"><use href="#i-people"/></svg></span><span class="rule" style="left:8px"></span>
      <h4>PROCESS</h4><p>Team Cadence</p><p class="b">Top | Down expectations</p><p>Bottom | Up expectations</p><p class="b">Forecast Methodology</p><p>Reporting Packages</p><p class="b">Old vs. New</p></div>
  </section>

  <!-- 12 90 day goals -->
  <section class="slide">
    <div class="abs" style="right:0;top:0;width:220px;height:312px;background:linear-gradient(200deg,#8a8f98 0%,#c7c9cd 40%,rgba(255,255,255,0) 70%)"></div>
    <div style="position:absolute;inset:0;opacity:.55">
      <div class="abs h-font" style="left:46px;top:16px;font-weight:700;font-size:17px;color:var(--ink)">30-60-90 Day Plan</div>
      <div class="plan-card" style="left:44px"><span class="hex" style="background:#8a8f98"><svg class="ic"><use href="#i-people"/></svg></span>
        <h4>PEOPLE</h4><p>Build Trust</p><p>Market Visits - Town Hall</p><p>Leadership Team</p><p>Direct Teams</p><p>Engineering Team</p><p>Dotted line resources</p></div>
      <div class="plan-card" style="left:370px"><span class="hex" style="background:#8a8f98"><svg class="ic"><use href="#i-people"/></svg></span>
        <h4>PROCESS</h4><p>Team Cadence</p><p>Top | Down expectations</p><p>Bottom | Up expectations</p><p>Forecast Methodology</p><p>Reporting Packages</p><p>Old vs. New</p></div>
    </div>
    <div class="abs" style="left:132px;top:14px;width:286px;height:286px;border-radius:50%;background:var(--white);box-shadow:0 3px 14px rgba(20,40,80,.3)"></div>
    <div class="abs" style="left:142px;top:24px;width:266px;height:266px;border-radius:50%;background:radial-gradient(circle at 40% 30%,var(--sky),var(--blue) 75%);color:var(--white)">
      <div style="width:22px;height:22px;margin:36px auto 0"><svg class="ic"><use href="#i-plane"/></svg></div>
      <div class="h-font" style="text-align:center;font-weight:700;font-size:9.5px;margin-top:8px">90 DAY GOALS</div>
      <div style="width:40px;height:1px;background:var(--white);margin:6px auto 10px"></div>
      <ol style="padding-left:58px;font-size:7.5px;line-height:13px">
        <li>Transition in rear view mirror</li>
        <li>Rhythm/Cadence in place</li>
        <li>Hit Plan in current Qtr</li>
        <li>Leadership engagement w/<br>&nbsp;&nbsp;• Top 15 Customers | Prospects</li>
        <li>Pipeline supports next Qtr</li>
        <li>Hire Key Roles</li>
      </ol>
    </div>
  </section>

  <!-- 13 FY define success -->
  <section class="slide" style="background:linear-gradient(180deg,var(--sky),var(--blue))">
    <div class="abs" style="left:122px;top:0;right:0;bottom:0;background:var(--white);border-top-left-radius:90px;border-bottom-left-radius:40px"></div>
    <div class="abs h-font" style="left:20px;top:162px;font-weight:600;font-size:19px;line-height:22px;color:var(--white)">FY –<br>Define<br>Success</div>
    <div class="abs" style="left:20px;top:232px;width:22px;height:2px;background:var(--white)"></div>
    <div class="fy-col" style="left:150px"><span class="blue-disc"><svg class="ic"><use href="#i-target"/></svg></span><div class="box">Hit Growth Targets</div><div class="drop"></div></div>
    <div class="fy-col" style="left:230px"><span class="blue-disc dark"><svg class="ic"><use href="#i-chart"/></svg></span><div class="box">Exceed Margin Guidance</div><div class="drop"></div></div>
    <div class="fy-col" style="left:310px"><span class="blue-disc"><svg class="ic"><use href="#i-gauge"/></svg></span><div class="box">Consistency in Execution &amp; Brilliant in the Basics</div><div class="drop"></div></div>
    <div class="fy-col" style="left:390px"><span class="blue-disc dark"><svg class="ic"><use href="#i-puzzle"/></svg></span><div class="box">Executive Relevance</div><div class="drop"></div></div>
    <div class="fy-col" style="left:470px"><span class="blue-disc"><svg class="ic"><use href="#i-doc"/></svg></span><div class="box">Vision and Plan set for Next Fiscal</div><div class="drop"></div></div>
    <svg class="abs" style="left:160px;top:250px" width="372" height="14" viewBox="0 0 372 14"><rect x="0" y="4" width="360" height="5" fill="#e3e7ee"/><path d="M358 0l12 7-12 7z" fill="#e3e7ee"/></svg>
  </section>

  <!-- 14 sponsors -->
  <section class="slide">
    <div class="abs" style="left:0;top:0;width:554px;height:150px;background:linear-gradient(180deg,#2c74bd,var(--sky) 60%,var(--aqua))" role="img" aria-label="Soft blue abstract backdrop"></div>
    <svg class="abs" style="left:0;top:100px" width="554" height="60" viewBox="0 0 554 60" preserveAspectRatio="none"><path d="M0 60 C150 10 380 60 554 0 V60 Z" fill="#fff"/></svg>
    <div class="abs h-font" style="left:0;right:0;top:50px;text-align:center;font-weight:700;font-size:18px;letter-spacing:1px;color:var(--white)">SPONSORS</div>
    <div class="sponsor" style="left:17px"><div class="face" role="img" aria-label="Portrait of sponsor"></div><h5>Maren Ashby</h5><p>SVP Americas<br>US Commercial<br>CORVEX</p></div>
    <div class="sponsor" style="left:119px"><div class="face" role="img" aria-label="Portrait of sponsor"></div><h5>Lena Voskuil</h5><p>VP<br>Global Services &amp;<br>Customer Experience<br>CORVEX</p></div>
    <div class="sponsor" style="left:221px"><div class="face" role="img" aria-label="Portrait of sponsor"></div><h5>Walt Brenner</h5><p>AVP Americas<br>Commercial West<br>CORVEX</p></div>
    <div class="sponsor" style="left:323px"><div class="face" role="img" aria-label="Portrait of sponsor"></div><h5>Reid Calloway</h5><p>AVP Enterprise West-Key<br>Segment</p></div>
    <div class="sponsor" style="left:425px"><div class="face" role="img" aria-label="Portrait of sponsor"></div><h5>Owen Pratt</h5><p>CMO<br>NORVALE</p></div>
  </section>

  <!-- 15 thank you -->
  <section class="slide">
    <div class="photo" style="inset:0;background:linear-gradient(150deg,#2d65ab 0%,#1d4c8c 50%,#163f78 100%)" role="img" aria-label="Blue backdrop with faint rising bar chart"></div>
    <div class="abs h-font" style="left:175px;top:136px;width:204px;height:40px;border:2px solid var(--white);text-align:center;font-weight:600;font-size:26px;line-height:36px;color:var(--white)">Thank you</div>
  </section>

  <!-- 16 appendix -->
  <section class="slide">
    <div class="photo" style="inset:0;background:radial-gradient(ellipse at 40% 90%,#2a5b8c 0%,#0f2545 45%,#060d1c 80%)" role="img" aria-label="Earth at night seen from orbit with city lights"></div>
    <div class="abs" style="left:40px;top:70px;width:304px;height:220px;border-radius:14px;background:rgba(51,166,215,.55)"></div>
    <div class="abs" style="left:40px;top:70px;width:304px;height:220px;border-radius:14px;border-top:2px solid rgba(255,255,255,.5);border-left:2px solid rgba(255,255,255,.5)"></div>
    <div class="abs h-font" style="left:82px;top:200px;font-weight:600;font-size:29px;color:var(--white)">Appendix</div>
  </section>

  <!-- 17 kairos -->
  <section class="slide">
    <div class="head"><h2>Word of the Qtr: Kairos</h2></div>
    <div class="head-sweep"></div>
    <div class="abs" style="left:38px;top:70px;width:478px;height:46px;border-radius:10px;box-shadow:0 1px 6px rgba(20,40,80,.18);background:var(--white)"></div>
    <div class="abs h-font" style="left:30px;top:54px;font-size:48px;font-weight:700;color:#8a94a6;line-height:48px">“</div>
    <div class="abs" style="left:66px;top:80px;font-size:8.5px;line-height:14px;color:var(--ink)">a time when conditions are right for the accomplishment of a crucial action: the<br>opportune and decisive moment</div>
    <div class="abs h-font" style="left:248px;top:94px;font-size:48px;font-weight:700;color:#8a94a6;line-height:48px">”</div>
    <div class="abs h-font" style="left:46px;top:148px;font-weight:700;font-size:11px;color:var(--ink)">FY20 Theme: &nbsp;Ride the Wave</div>
    <ul class="abs" style="left:48px;top:174px;width:330px;font-size:6.8px;line-height:8.6px;color:var(--ink);list-style:none">
      <li style="margin-bottom:5px">➢ FY20 will begin with a <b>Wave</b> of significant <b>Change</b></li>
      <li style="margin-bottom:5px">➢ Why this as a theme? “From a Non-Surfer”</li>
      <li style="margin-bottom:5px">➢ Tide matters, wind matters, waves matter (external factors)</li>
      <li style="margin-bottom:5px">➢ Takes a lot of work and energy to paddle out (you have to want it)</li>
      <li style="margin-bottom:5px">➢ Lots of dangers(competitors) reef, rip tides, sharks, other surfers</li>
      <li>➢ Right wave, right height, go with the wave, lean into it, enjoy the ride.<br>&nbsp;&nbsp;&nbsp;Make the paddle out-worth it!</li>
    </ul>
    <div class="photo" style="left:404px;top:152px;width:118px;height:118px;border-radius:50%;background:radial-gradient(circle,#ffffff 40%,var(--mist) 60%,var(--blue) 62%,var(--deep) 100%)" role="img" aria-label="Circular team emblem with a surfer riding a wave"></div>
  </section>

  <!-- 18 gold standard -->
  <section class="slide">
    <div class="abs h-font" style="left:0;right:0;top:12px;text-align:center;font-weight:500;font-size:12.5px;color:var(--blue)">Select “Excellence in Role or The Gold Standard”</div>
    <div class="abs" style="left:16px;top:58px;width:1px;height:244px;border-left:1px dashed #98a4b6"></div>
    <div class="abs" style="left:16px;top:58px;width:160px;border-top:1px dashed #98a4b6"></div>
    <div class="abs" style="left:20px;top:62px;width:172px;font-size:6.3px;line-height:8px;color:var(--ink)">
      <div class="h-font" style="font-weight:700;font-size:7.5px;margin-bottom:5px">GTM</div>
      <p>Leverage the power of ONECorvex</p>
      <p>Planning and regular cadence with extended team and virtual sales</p>
      <p>Scale through partners</p>
      <p style="margin-bottom:4px">Leverage programs to build pipeline</p>
      <div class="h-font" style="font-weight:600;font-size:7.5px;color:var(--sky);margin-bottom:4px">Architectures &amp; Solutions</div>
      <p>Utilize account data and knowledge of customer business models to capture market transitions</p>
      <p>Protect the base- aggressively pursue all LDOS and renewals in account base.</p>
      <p>Builds migration path to RSW solutions vs boxes (Quote 3 and sell 1 EA)</p>
      <p>Leverage channel and extended team to sell to IT</p>
      <p>Utilize BE Heat Map across accounts</p>
    </div>
    <svg class="abs" style="left:196px;top:100px" width="170" height="170" viewBox="-85 -85 170 170">
      <path d="M0 -80 A80 80 0 0 1 80 0 L40 0 A40 40 0 0 0 0 -40 Z" fill="#1c4f8e"/>
      <path d="M80 0 A80 80 0 0 1 0 80 L0 40 A40 40 0 0 0 40 0 Z" fill="#3377b5"/>
      <path d="M0 80 A80 80 0 0 1 -80 0 L-40 0 A40 40 0 0 0 0 40 Z" fill="#85acd3"/>
      <path d="M-80 0 A80 80 0 0 1 0 -80 L0 -40 A40 40 0 0 0 -40 0 Z" fill="#2b2f36"/>
      <g stroke="#fff" stroke-width="3"><path d="M0 -85V-38M85 0H38M0 85V38M-85 0H-38"/></g>
      <g fill="none" stroke="#fff" stroke-width="1.8">
        <path d="M-36 -50a9 9 0 1 1 10 0v5h-10z"/>
        <path d="M30 -38h24M34 -38v-14M42 -38v-20M50 -38v-10"/>
        <path d="M-46 34l10-6 10 6-10 6z M-46 34v12l10 6v-12M-26 34v12l-10 6"/>
        <circle cx="34" cy="36" r="4"/><circle cx="46" cy="36" r="4"/><path d="M28 52c0-6 3-9 6-9s6 3 6 9M40 52c0-6 3-9 6-9s6 3 6 9"/>
      </g>
    </svg>
    <div class="abs" style="left:374px;top:68px;width:1px;height:244px;border-left:1px dashed #98a4b6"></div>
    <div class="abs" style="left:374px;top:68px;width:160px;border-top:1px dashed #98a4b6"></div>
    <div class="abs" style="left:380px;top:72px;width:160px;text-align:right;font-size:6.3px;line-height:8px;color:var(--ink)">
      <div class="h-font" style="font-weight:700;font-size:8px;margin-bottom:5px;color:var(--navy)">Operational Excellence</div>
      <p>Stretch vs. Hero forecasting- 70% commit w risk</p>
      <p>Thorough deal assurance knowledge</p>
      <p>Comprehensive territory plans with Qtrly milestones</p>
      <p>No past due opportunities</p>
      <p>All opportunities have technology and SE assigned</p>
      <p style="margin-bottom:6px">Leverage GFEP for Post-Sales Support</p>
      <div class="h-font" style="font-weight:600;font-size:7.5px;color:var(--sky);margin-bottom:4px">Training &amp; Development</div>
      <p>Aligned to forecast confidence guidelines</p>
      <p>Leveraging account plan template and heatmap</p>
      <p>Completes mandated corporate and SP training</p>
      <p>Contributes and makes an impact beyond role</p>
      <p>Leverage the regional SE Lab</p>
    </div>
  </section>

  <!-- 19 leadership expectations 1 -->
  <section class="slide">
    <div class="head"><h2 style="font-size:15px">Leadership Expectations–Sales Leaders</h2></div>
    <div class="head-sweep"></div>
    <div class="chev" style="left:28px;width:180px">
      <svg class="shape" viewBox="0 0 180 190" preserveAspectRatio="none"><path d="M2 2H150L178 95L150 188H2L30 95Z" fill="#f5f7fa" stroke="#d5dbe4"/></svg>
      <div class="inner"><h5>Be a Culture Builder</h5><div class="icon"><svg class="ic"><use href="#i-paperclip"/></svg></div>
        <ul><li>Personal Humility and Professional Will (Be a role model)</li><li>Engage others in shared meaning</li><li>Scale through influence</li></ul></div>
    </div>
    <div class="chev" style="left:188px;width:180px">
      <svg class="shape" viewBox="0 0 180 190" preserveAspectRatio="none"><path d="M2 2H150L178 95L150 188H2L30 95Z" fill="#f5f7fa" stroke="#d5dbe4"/></svg>
      <div class="inner"><h5>Own the Number and the Details</h5><div class="icon"><svg class="ic"><use href="#i-heart"/></svg></div>
        <ul><li>Demonstrate sustainable value to our customers, partners and corvex team</li><li>Timely communication | Limit surprises | High Care Factor</li><li>Know our business | Ensure each IC contributes to knowing the business</li></ul></div>
    </div>
    <div class="chev" style="left:348px;width:180px">
      <svg class="shape" viewBox="0 0 180 190" preserveAspectRatio="none"><path d="M2 2H150L178 95L150 188H2L30 95Z" fill="#f5f7fa" stroke="#d5dbe4"/></svg>
      <div class="inner"><h5>Contribute Beyond Region Objectives</h5><div class="icon"><svg class="ic"><use href="#i-puzzle"/></svg></div>
        <ul><li>Be part of the solution</li><li>Share a better idea (Better to light a candle than curse the darkness)</li><li>Make each other successful</li></ul></div>
    </div>
  </section>

  <!-- 20 leadership expectations 2 -->
  <section class="slide">
    <div class="head"><h2 style="font-size:15px">Leadership Expectations–Sales Leaders</h2></div>
    <div class="head-sweep"></div>
    <div class="chev" style="left:108px;width:180px">
      <svg class="shape" viewBox="0 0 180 190" preserveAspectRatio="none"><path d="M2 2H150L178 95L150 188H2L30 95Z" fill="#f5f7fa" stroke="#d5dbe4"/></svg>
      <div class="inner"><h5>Grow in Role</h5><div class="icon"><svg class="ic"><use href="#i-chart"/></svg></div>
        <ul><li>If you aren’t learning you aren’t moving forward</li><li>Positively influence the learning of others</li><li>What’s next discussion bi-annually? (own your development plan)</li></ul></div>
    </div>
    <div class="chev" style="left:268px;width:180px">
      <svg class="shape" viewBox="0 0 180 190" preserveAspectRatio="none"><path d="M2 2H150L178 95L150 188H2L30 95Z" fill="#fcf7c1" stroke="#eadf9c"/></svg>
      <div class="inner"><h5>Live by the Golden Rule</h5><div class="icon"><svg class="ic"><use href="#i-medal"/></svg></div>
        <ul><li>Don’t tolerate intolerable behavior</li><li>Don’t let people waste other people’s time</li><li>Say Thank-you often</li></ul></div>
    </div>
  </section>

  <!-- 21 career timeline -->
  <section class="slide" style="background:linear-gradient(180deg,var(--sky),var(--blue))">
    <div class="abs" style="left:122px;top:0;right:0;bottom:0;background:var(--white);border-top-left-radius:90px;border-bottom-left-radius:40px"></div>
    <div class="abs h-font" style="left:12px;top:192px;font-weight:600;font-size:15px;line-height:18px;color:var(--white)">CAREER:<br>TIMELINE</div>
    <div class="abs" style="left:12px;top:236px;width:22px;height:2px;background:var(--white)"></div>
    <div class="tl-logo" style="top:18px"><i></i>Harbor Guard</div>
    <div class="tl-logo" style="top:60px">Stafflane</div>
    <div class="tl-logo" style="top:100px">Givewell Systems</div>
    <div class="tl-logo" style="top:141px">Corvex</div>
    <div class="abs" style="left:273px;top:10px;width:1px;height:296px;border-left:1px dashed #98a4b6"></div>
    <div class="tl-year" style="top:16px">1993</div><div class="tl-text" style="top:20px">Officer, Harbor Guard</div>
    <div class="tl-year" style="top:59px">1999</div><div class="tl-text" style="top:63px">Account Manager, Branch Manager and Area Director</div>
    <div class="tl-year" style="top:98px">2004</div><div class="tl-text" style="top:98px">Inside Sales Manager, Outside Sales Manager, General Manager</div>
    <div class="tl-year" style="top:139px">2014</div><div class="tl-text" style="top:139px">Regional Manager, Southwest Territory<br>Regional Manager, Metro Philly Select</div>
    <div class="tl-year" style="top:181px">2017</div><div class="tl-text" style="top:185px">Operations Director, Service Provider US</div>
    <div class="tl-year" style="top:222px">2019</div><div class="tl-text" style="top:226px">Operations Director, Mid Markets Select</div>
    <div class="tl-year now" style="top:264px">2020</div><div class="tl-text" style="top:268px">Add your text here</div>
  </section>

  <!-- 22 icon library -->
  <section class="slide">
    <div class="abs h-font" style="left:0;right:0;top:20px;text-align:center;font-weight:600;font-size:15px;color:var(--deep)">Free editable vector icon links available</div>
    <div class="photo" style="left:26px;top:58px;width:502px;height:232px;border-radius:4px;background:linear-gradient(135deg,var(--mist),#e8eff7 50%,var(--mist))" role="img" aria-label="Library of blue line icons arranged in a grid"></div>
  </section>

</main>
</body>
</html>
```